THE 4 (THREE-SIDED) PYRAMIDS OF "THE 5 ORBITS"

I WOULD LIKE TO CREATE DESIGN FOR MY 4 "TRILATERAL" (THREE-SIDED) PYRAMIDS WHICH MAKE UP THE 5 ORBITS. IN ADDITION I WOULD LIKE TO SEE DESIGNS WITH THE PYRAMIDS OVERLAPPING AT 30 DEGREES. THESE DESIGNS NEED TO BE ABLE TO COPY AND PASTED ON MULTIPLE DIFFERENT APPLICATIONS

Font styles to use
Sans Serif

Colors
6b439a
00a990
ec1f27
3277b5

Requirements
Must have
• EACH PYRAMID HAS A DESIGNATED COLOR. THE 1ST PYRAMID IS PURPLE- THE HIGHEST LEVEL SHOULD BE DARK PURPLE AND THE LOWER LEVELS DECRESING SHADES OF PURPLE. THIS SHOULD BE REPEATED FOR THE GREEEN, RED AND BLUE PYRAMIDS. EACH CORNER OF EVERY LEVEL SHOULD HAVE THE WORD OR WORDS AFFILIATED TO THAT CONNER LABELLED

```html
<!DOCTYPE html>
<html lang="en">
<head>
<meta charset="UTF-8">
<title>The Pyramid of I AM</title>
<link href="https://fonts.googleapis.com/css2?family=Source+Sans+3:wght@700&display=swap" rel="stylesheet">
<style>
  :root {
    --bg: #ffffff;
    --label: #9a9ca3;
    --inner-label: #e3e6ec;
    --band: #16234d;
    --level-1: #16234d;
    --level-2: #1c325b;
    --level-3: #22436f;
    --level-4: #32547f;
    --level-5: #456893;
    --level-6: #5378a6;
    --level-7: #6689ba;
    --spine: #2e4a78;
  }
  html, body {
    margin: 0;
    padding: 0;
    width: 1200px;
    height: 1000px;
    overflow: hidden;
    background: var(--bg);
  }
  .canvas {
    width: 1200px;
    height: 1000px;
    display: block;
  }
  .pyramid text {
    font-family: "Source Sans 3", "Myriad Pro", Arial, sans-serif;
    font-weight: 700;
    font-size: 29px;
    letter-spacing: -0.3px;
  }
  .corner-label { fill: var(--label); }
  .corner-label.left { text-anchor: end; }
  .corner-label.right { text-anchor: start; }
  .corner-label.centre { text-anchor: middle; }
  .pyramid .summit-label { fill: var(--label); text-anchor: middle; font-size: 36px; }
  .level-name { fill: var(--inner-label); text-anchor: middle; }
  .band { fill: var(--band); stroke: var(--band); stroke-width: 3; stroke-linejoin: round; }
  .level { stroke-width: 6; stroke-linejoin: round; }
  .level-1 { fill: var(--level-1); stroke: var(--level-1); }
  .level-2 { fill: var(--level-2); stroke: var(--level-2); }
  .level-3 { fill: var(--level-3); stroke: var(--level-3); }
  .level-4 { fill: var(--level-4); stroke: var(--level-4); }
  .level-5 { fill: var(--level-5); stroke: var(--level-5); }
  .level-6 { fill: var(--level-6); stroke: var(--level-6); }
  .level-7 { fill: var(--level-7); stroke: var(--level-7); }
  .spine { stroke: var(--spine); stroke-width: 9; opacity: 0.55; }
</style>
</head>
<body>
<svg class="canvas pyramid" viewBox="0 0 2100 1750" width="1200" height="1000" xmlns="http://www.w3.org/2000/svg" aria-label="Seven-level pyramid rising to I AM">

  <!-- separating bands between levels -->
  <g class="bands">
    <polygon class="band" points="908,365 1024,396 1140,365 1152,381 1024,412 896,381"/>
    <polygon class="band" points="832,465 1024,516 1216,465 1228,481 1024,532 820,481"/>
    <polygon class="band" points="759,560 1024,630 1289,560 1301,576 1024,646 747,576"/>
    <polygon class="band" points="670,678 1024,772 1378,678 1390,694 1024,788 658,694"/>
    <polygon class="band" points="551,835 1024,961 1497,835 1509,851 1024,977 539,851"/>
    <polygon class="band" points="406,1025 1024,1189 1642,1025 1654,1041 1024,1205 394,1041"/>
  </g>

  <!-- levels, top to bottom -->
  <g class="levels">
    <polygon class="level level-1" points="1024,215 1138,365 1024,394 910,365"/>
    <polygon class="level level-2" points="898,383 1024,414 1150,383 1213,465 1024,514 835,465"/>
    <polygon class="level level-3" points="822,483 1024,534 1226,483 1286,560 1024,628 762,560"/>
    <polygon class="level level-4" points="749,578 1024,648 1299,578 1375,678 1024,770 673,678"/>
    <polygon class="level level-5" points="660,696 1024,790 1388,696 1494,835 1024,959 554,835"/>
    <polygon class="level level-6" points="541,853 1024,979 1507,853 1639,1025 1024,1187 409,1025"/>
    <polygon class="level level-7" points="396,1043 1024,1207 1652,1043 1798,1235 1024,1438 250,1235"/>
  </g>

  <line class="spine" x1="1024" y1="218" x2="1024" y2="1436"/>

  <!-- summit -->
  <text class="summit-label" x="1028" y="198">I AM</text>

  <!-- level names -->
  <text class="level-name" x="1024" y="406">THE WAY</text>
  <text class="level-name" x="1024" y="525">CHARITY</text>
  <text class="level-name" x="1024" y="647">TRUST</text>
  <text class="level-name" x="1026" y="766">PURE</text>
  <text class="level-name" x="1028" y="794">CONSCIOUSNESS</text>
  <text class="level-name" x="1024" y="981">JUDGMENT</text>
  <text class="level-name" x="1024" y="1187">THE SANDAL</text>
  <text class="level-name" x="1024" y="1215">OF PEACE</text>

  <!-- left corners -->
  <text class="corner-label left" x="900" y="370">THE TRUTH</text>
  <text class="corner-label left" x="829" y="440">GENTLENESS</text>
  <text class="corner-label left" x="829" y="468">MEEKNESS</text>
  <text class="corner-label left" x="750" y="567">REST</text>
  <text class="corner-label left" x="653" y="656">PURE</text>
  <text class="corner-label left" x="653" y="684">POTENTIALITY</text>
  <text class="corner-label left" x="537" y="814">GUILT</text>
  <text class="corner-label left" x="537" y="848">(SHAME)</text>
  <text class="corner-label left" x="398" y="1006">THE BELT</text>
  <text class="corner-label left" x="398" y="1034">OF TRUTH</text>
  <text class="corner-label left" x="235" y="1225">THE FIRST</text>
  <text class="corner-label left" x="240" y="1260">AND THE LAST</text>

  <!-- right corners -->
  <text class="corner-label right" x="1148" y="370">THE LIFE</text>
  <text class="corner-label right" x="1225" y="440">LONG-SUFFERING</text>
  <text class="corner-label right" x="1225" y="468">PATIENCE</text>
  <text class="corner-label right" x="1302" y="567">WAIT</text>
  <text class="corner-label right" x="1390" y="656">PURE</text>
  <text class="corner-label right" x="1390" y="684">BLISS</text>
  <text class="corner-label right" x="1512" y="814">SIN</text>
  <text class="corner-label right" x="1512" y="848">(TEMPTATION)</text>
  <text class="corner-label right" x="1652" y="1006">THE SWORD</text>
  <text class="corner-label right" x="1652" y="1034">OF THE SPIRIT</text>
  <text class="corner-label right" x="1816" y="1225">THE BEGINNING</text>
  <text class="corner-label right" x="1816" y="1260">AND THE END</text>

  <!-- base point -->
  <text class="corner-label centre" x="1024" y="1472">THE ALPHA AND</text>
  <text class="corner-label centre" x="1024" y="1507">THE OMEGA</text>
</svg>
</body>
</html>
```